Cards
Brookvale Estate Advisors
Cards - Real Estate
Creative Brief
Modern
Teodoro Villalba
Managing Broker
4870 Hollow Ln. Wrenfield IN 46958
closedbytv@quellmark.com
I also need the Homeward/MLS logo, along with the Fair Dwelling logo

```html
<!DOCTYPE html>
<html lang="en">
<head>
<meta charset="utf-8">
<title>Brookvale Estate Advisors – Business Card</title>
<link rel="stylesheet" href="https://fonts.googleapis.com/css2?family=Tinos:wght@400;700&display=swap">
<style>
  :root {
    --backdrop: #2b2b2b;
    --card: #ffffff;
    --green: #6aa728;
    --blue: #2c7bbf;
    --ink: #2a2a2a;
    --rule: #bdbdbd;
    --badge: #3a3a3a;
  }
  * { margin: 0; padding: 0; box-sizing: border-box; }
  html, body { width: 1200px; height: 780px; overflow: hidden; }
  body {
    background: var(--backdrop);
    font-family: "Tinos", "Times New Roman", serif;
    position: relative;
  }
  .business-card {
    position: absolute;
    left: 100px; top: 104px;
    width: 1000px; height: 572px;
    background: var(--card);
    border-radius: 34px;
    overflow: hidden;
  }
  .edge-band {
    position: absolute; left: 0; top: 0; bottom: 0;
    width: 26px; background: var(--green);
  }
  .edge-line {
    position: absolute; left: 30px; top: 0; bottom: 0;
    width: 5px; background: var(--blue);
  }
  .membership-badges {
    position: absolute; right: 42px; top: 30px;
    display: flex; gap: 14px;
  }
  .badge { width: 44px; height: 44px; background: var(--badge); border-radius: 4px; }
  .badge.wide { width: 92px; }
  .brand {
    position: absolute; left: 270px; top: 150px;
    display: flex; align-items: center; gap: 22px;
  }
  .brand-mark { width: 70px; height: 70px; background: var(--green); flex: none; }
  .brand-name {
    color: var(--ink);
    font-weight: 400;
    text-transform: uppercase;
    line-height: 1.05;
  }
  .brand-name .line-main { display: block; font-size: 58px; letter-spacing: 1px; }
  .brand-name .line-sub { display: block; font-size: 32px; letter-spacing: 0.5px; }
  .agent {
    position: absolute; right: 560px; top: 350px;
    text-align: right;
    white-space: nowrap;
  }
  .agent-name { color: var(--green); font-size: 34px; font-weight: 700; }
  .agent-title { color: var(--blue); font-size: 24px; margin-top: 6px; }
  .agent-address { color: var(--ink); font-size: 24px; margin-top: 14px; line-height: 1.25; }
  .divider {
    position: absolute; left: 462px; top: 350px;
    width: 2px; height: 150px; background: var(--rule);
  }
  .contact-list {
    position: absolute; left: 482px; top: 340px;
    list-style: none;
  }
  .contact-list li {
    display: flex; align-items: center; gap: 14px;
    font-size: 23px; color: var(--ink); height: 38px;
    white-space: nowrap;
  }
  .contact-list svg { width: 22px; height: 22px; fill: var(--green); flex: none; }
</style>
</head>
<body>
  <div class="business-card">
    <div class="edge-band"></div>
    <div class="edge-line"></div>

    <div class="membership-badges">
      <div class="badge wide" role="img" aria-label="Homeward MLS membership badge"></div>
      <div class="badge" role="img" aria-label="Fair Dwelling badge"></div>
    </div>

    <div class="brand">
      <div class="brand-mark"></div>
      <div class="brand-name">
        <span class="line-main">Brookvale</span>
        <span class="line-sub">Estate Advisors</span>
      </div>
    </div>

    <div class="agent">
      <div class="agent-name">Teodoro Villalba</div>
      <div class="agent-title">Managing Broker</div>
      <div class="agent-address">4870 Hollow Ln.<br>Wrenfield IN 46958</div>
    </div>

    <div class="divider"></div>

    <ul class="contact-list">
      <li>
        <svg viewBox="0 0 24 24" aria-hidden="true"><path d="M6.6 10.8a15.1 15.1 0 0 0 6.6 6.6l2.2-2.2a1 1 0 0 1 1-.25 11.4 11.4 0 0 0 3.6.57 1 1 0 0 1 1 1V20a1 1 0 0 1-1 1A17 17 0 0 1 3 4a1 1 0 0 1 1-1h3.5a1 1 0 0 1 1 1c0 1.25.2 2.45.57 3.57a1 1 0 0 1-.25 1z"/></svg>
        555-204-3817
      </li>
      <li>
        <svg viewBox="0 0 24 24" aria-hidden="true"><path d="M7 2h10a2 2 0 0 1 2 2v16a2 2 0 0 1-2 2H7a2 2 0 0 1-2-2V4a2 2 0 0 1 2-2zm0 3v12h10V5zm5 13.5a1.2 1.2 0 1 0 0 2.4 1.2 1.2 0 0 0 0-2.4z"/></svg>
        555-671-2093
      </li>
      <li>
        <svg viewBox="0 0 24 24" aria-hidden="true"><path d="M7 2h10v6H7zM4 9h16a2 2 0 0 1 2 2v7h-4v4H6v-4H2v-7a2 2 0 0 1 2-2zm4 8v3h8v-3z"/></svg>
        555-318-7460
      </li>
      <li>
        <svg viewBox="0 0 24 24" aria-hidden="true"><path d="M3 5h18a1 1 0 0 1 1 1v12a1 1 0 0 1-1 1H3a1 1 0 0 1-1-1V6a1 1 0 0 1 1-1zm1 2.3V17h16V7.3l-8 5.2z M4.6 7 12 11.8 19.4 7z"/></svg>
        closedbytv@quellmark.com
      </li>
    </ul>
  </div>
</body>
</html>
```